Belle Lueur Hand Crafted Candles promotional flyer

Hand Crafted Soy Candles - I need a flyer to promote my candles and to give information on care of candles.I want this to use the design and colours I already have for my labels and the photo I have attached.I am aiming at a sophisticated market so would like to reflect this in the design.
Should appeal to sophisticated women who enjoy the pleasure of candles - to enhance their enjoyment of life - gives them the 'Belle Lueur'.
the candles are hand crafted from all natural ingredients, environmentally friendly and with exquisite fragrances

Target Market(s)

sophisticated females

Industry/Entity Type

Promotional

Font styles to use
Script

Colors
cfeae6
ecdaeb

Requirements
Must have
• something expressing 'Belle Lueur' - the enjoyment of candles
Should not have
• bright colours

```html
<!DOCTYPE html>
<html lang="en">
<head>
<meta charset="utf-8">
<title>Belle Lueur Hand Crafted Candles – Flyer</title>
<link href="https://fonts.googleapis.com/css2?family=Great+Vibes&family=Crimson+Text:wght@400;600;700&display=swap" rel="stylesheet">
<style>
  :root {
    --teal: #9fd5cb;
    --teal-soft: #cfeae6;
    --lilac: #c79ac6;
    --lilac-soft: #ecdaeb;
    --ink: #3a3a3a;
    --ink-soft: #555;
    --paper: #ffffff;
    --panel-edge: #d9d9d9;
  }
  * { box-sizing: border-box; margin: 0; padding: 0; }
  html, body { width: 907px; height: 1200px; overflow: hidden; background: var(--paper); }
  body { font-family: "Crimson Text", Georgia, serif; color: var(--ink); }

  .flyer { position: relative; width: 907px; height: 1200px; overflow: hidden; background: var(--paper); }
  .backdrop { position: absolute; inset: 0; }

  .hero-photo {
    position: absolute; left: 312px; top: 0; width: 595px; height: 290px;
    background: radial-gradient(ellipse at 60% 45%, #f0d9cc 0%, #e8c9b8 30%, #f6efec 65%, #ffffff 100%);
  }
  .brand-mark {
    position: absolute; left: 28px; top: 52px; width: 190px;
    display: flex; flex-direction: column; align-items: center; gap: 10px;
  }
  .brand-mark .dot { width: 14px; height: 14px; border-radius: 50%; background: var(--lilac); }
  .brand-mark .name { font-size: 22px; font-weight: 400; color: var(--ink-soft); text-align: center; line-height: 1.25; }

  .product-photo {
    position: absolute; left: 18px; top: 300px; width: 455px; height: 205px; border-radius: 6px;
    background: linear-gradient(90deg, #e8e6df 0%, #2f3540 35%, #eae7de 65%, #3b3f86 100%);
    opacity: .85;
  }

  .headline { position: absolute; left: 60px; top: 548px; width: 400px; text-align: center; }
  .headline .script { font-family: "Great Vibes", cursive; font-size: 68px; color: #2a2a2a; line-height: 1; }
  .headline .tagline { font-size: 24px; color: #333; margin-top: 0; padding-bottom: 6px; border-bottom: 1px solid #555; display: inline-block; }

  .intro { position: absolute; left: 34px; top: 686px; width: 420px; font-size: 16.5px; line-height: 1.5; color: var(--ink-soft); }
  .intro p { text-align: justify; margin-bottom: 12px; }

  .pill {
    display: inline-block; font-weight: 700; font-size: 18px; color: #333;
    padding: 5px 24px 5px 28px; border-radius: 0 20px 20px 0;
    background: linear-gradient(90deg, rgba(236,218,235,0) 0%, var(--lilac-soft) 35%, var(--lilac) 100%);
  }
  .refill { position: absolute; left: 0; top: 876px; width: 470px; }
  .refill ul { list-style: none; padding: 20px 0 0 36px; }
  .refill li { position: relative; padding-left: 18px; font-size: 16px; line-height: 1.45; color: var(--ink-soft); margin-bottom: 7px; }
  .refill li::before { content: ""; position: absolute; left: 0; top: 9px; width: 6px; height: 6px; border-radius: 50%; background: #444; }

  .care {
    position: absolute; left: 478px; top: 351px; width: 392px; height: 740px; border-radius: 10px;
    background: linear-gradient(90deg, #ffffff 0%, #fafafa 55%, #dcdcdc 100%);
    box-shadow: 0 0 3px rgba(0,0,0,.12);
  }
  .care .pill { position: absolute; right: 40px; top: 14px; border-radius: 20px; padding: 5px 22px; font-size: 17px;
    background: linear-gradient(90deg, rgba(236,218,235,.2) 0%, var(--lilac-soft) 40%, var(--lilac) 100%); }
  .care ul { list-style: none; padding: 72px 22px 0 24px; }
  .care li { position: relative; padding-left: 20px; font-size: 17.5px; line-height: 1.4; text-align: justify; color: var(--ink); margin-bottom: 13px; }
  .care li::before { content: ""; position: absolute; left: 0; top: 9px; width: 8px; height: 8px; border-radius: 50%; background: #444; }

  .contact { position: absolute; left: 400px; top: 1112px; width: 480px; font-weight: 700; font-size: 19px; color: #2c2c2c; }
  .contact .row { display: flex; align-items: center; gap: 8px; }
  .contact .row.top { justify-content: space-between; }
  .contact .row.web { justify-content: center; margin-top: 8px; }
  .contact .item { display: flex; align-items: center; gap: 8px; }
  .contact svg { width: 18px; height: 18px; fill: #2c2c2c; }
</style>
</head>
<body>
<main class="flyer">
  <svg class="backdrop" width="907" height="1200" viewBox="0 0 907 1200" aria-hidden="true">
    <defs>
      <linearGradient id="tealWash" x1="0" y1="0" x2="0" y2="1">
        <stop offset="0" stop-color="#f3fbf9"/>
        <stop offset=".35" stop-color="#9fd5cb"/>
        <stop offset="1" stop-color="#e8f6f3"/>
      </linearGradient>
      <linearGradient id="lilacBand" x1="0" y1="0" x2="1" y2="0">
        <stop offset="0" stop-color="#f2e6f1"/>
        <stop offset="1" stop-color="#c79ac6"/>
      </linearGradient>
      <linearGradient id="lilacFoot" x1="0" y1="0" x2="1" y2="0">
        <stop offset="0" stop-color="#c79ac6"/>
        <stop offset=".5" stop-color="#ecdaeb"/>
        <stop offset="1" stop-color="#c79ac6"/>
      </linearGradient>
    </defs>
    <rect width="907" height="1200" fill="#fff"/>
    <!-- teal body wash -->
    <path d="M0 470 C200 520 420 470 907 330 L907 1100 L0 1100 Z" fill="url(#tealWash)"/>
    <!-- lilac swoosh under hero -->
    <path d="M0 330 C250 360 520 330 907 250 L907 300 C560 370 300 410 0 400 Z" fill="url(#lilacBand)"/>
    <path d="M0 400 C300 410 560 370 907 300 L907 325 C560 395 300 440 0 430 Z" fill="#fff" opacity=".85"/>
    <!-- lilac under products -->
    <path d="M0 480 C150 500 320 520 470 500 L470 545 C320 560 150 545 0 520 Z" fill="#ecdaeb"/>
    <!-- arc near logo -->
    <path d="M260 0 C350 60 360 200 300 300" stroke="#9fd5cb" stroke-width="4" fill="none"/>
    <path d="M250 0 C330 50 340 170 290 270" stroke="#ecdaeb" stroke-width="3" fill="none"/>
    <!-- footer band -->
    <path d="M0 1090 C250 1060 600 1140 907 1080 L907 1200 L0 1200 Z" fill="url(#lilacFoot)"/>
    <path d="M0 1095 C250 1068 600 1148 907 1090 L907 1100 C600 1160 250 1080 0 1108 Z" fill="#fff" opacity=".7"/>
  </svg>

  <div class="hero-photo" role="img" aria-label="Photograph of a relaxed woman resting her head on her folded arms"></div>

  <div class="brand-mark">
    <span class="dot"></span>
    <span class="name">Belle Lueur<br>Hand Crafted Candles</span>
  </div>

  <div class="product-photo" role="img" aria-label="Photograph of four labelled soy candles in glass containers"></div>

  <header class="headline">
    <div class="script">Belle Lueur</div>
    <div class="tagline">an exuberant enjoyment of life</div>
  </header>

  <section class="intro">
    <p>Hand crafted soy candle creations are lovingly hand-poured and use only the finest of ingredients and fragrances. Soft smooth wax burns clear and up to 50% longer than traditional paraffin candles.</p>
    <p>Made form soya beans, a renewable natural resource that supports and sustains agriculture – it is biodegradable and environmentally friendly.</p>
  </section>

  <section class="refill">
    <h2 class="pill">Containers can be refilled</h2>
    <ul>
      <li>I offer a refill service -if you return you containers to me I can refill with the fragrance of your choice</li>
      <li>Or if you have a special container you would like to use for your candle just contact me for a quote.</li>
      <li>I have a wide range of fragrances - please<br>contact me for details.</li>
    </ul>
  </section>

  <section class="care">
    <h2 class="pill">How to care for your candle</h2>
    <ul>
      <li>When lighting you candle for the first time, allow the wax to melt all the way to the sides of the container – this creates a ‘memory’ and avoids ‘tunnelling’ as the candle burns.</li>
      <li>Always trim the wick to about 6-8mm before re-lighting your candle to ensure a long lasting candle.</li>
      <li>It is preferable to use a candle ‘snuffer’ to extinguish the flame, or a lid if the candle has one.</li>
      <li>All Belle Lueur candles are hand poured not massed produced so every candle may be different.</li>
      <li>Sometimes you may notice darker patches or wet spots - it does not affect the candle in anyway.</li>
      <li>The top of the candle may also appear slightly uneven – this is just a sign of natural soy wax being hand poured.</li>
      <li>Do not leave your candle in the sunlight as it may turn a yellow colour.</li>
      <li>As these candles contain no preservatives or chemicals it is recommended that they should be used within 6 months.</li>
    </ul>
  </section>

  <footer class="contact">
    <div class="row top">
      <span class="item">
        <svg viewBox="0 0 24 24" aria-hidden="true"><path d="M2 5h20v14H2z M3 6l9 7 9-7" fill="#2c2c2c"/><path d="M3 6.5l9 7 9-7" stroke="#fff" stroke-width="1.5" fill="none"/></svg>
        claire.marsh@bellelueur.co.nz
      </span>
      <span class="item">
        <svg viewBox="0 0 24 24" aria-hidden="true"><path d="M6.6 2.5l3 3.5-2 2.4c1.2 2.6 3.4 4.8 6 6l2.4-2 3.5 3-1.8 3.6C10 18.5 5.5 14 3 6.3z"/></svg>
        021 555 0148
      </span>
    </div>
    <div class="row web">
      <svg viewBox="0 0 24 24" aria-hidden="true"><circle cx="12" cy="12" r="10"/><path d="M2 12h20M12 2c3 3 3 17 0 20M12 2c-3 3-3 17 0 20" stroke="#fff" stroke-width="1.4" fill="none"/></svg>
      www.bellelueurcandles.co.nz
    </div>
  </footer>
</main>
</body>
</html>
```